Business school needs a web design

Who We are:
KRVT is a small business school that offers programs in Project Management. The school is based in West Africa and welcomes students from the whole area. Our aim is to become one of the reference business schools in Africa.

Project Brief:
The site will include all informations relevant for different types of visitors that we have: actual and future students, companies, mass media, future employees, ect. It will present information about subscription, list of programs, presentation of the school and its team,etc.

What We want:
This competition is for Design only no coding! We need design for two pages.
We did some wireframing for the home page and the list of programs page. We made them just to show how we imagine the website would look like. But we encourage creative designs, so you don't have to stick to the wireframe models.

Sites We like:
http://www.ravenmoorcollege.example/
http://www.belvantis.example/fr/etudes.html
http://www.qtl.example/mba/Pages/default.aspx

Color schemes
The logo of the school is red and black. So the color scheme of the website should match that. For the rest, it is opened to your imagination.
Updates

The payment for the project is now garanteed. Good luck to you all !

Target Market(s)

The target market is diversified because we have students of different ages, also company representatives or employees that might visit the website for recruitment purposes. But the majority of our audience should be aged between 20 - 30 years.

Industry/Entity Type

Small Business

Requirements
Must have
• The design must include two pages: a home page and another interior page : might be the list of programs or any other page relevant to the domain. The Home page must include a slide show at the beginning.
The background page must be white.
Nice to have
• The use of flat design for this project is preferred.
The use of Pelican scaffold as a base for the design is an asset.

```html
<!DOCTYPE html>
<html lang="fr">
<head>
<meta charset="utf-8">
<title>KRVT – Programmes et Formation</title>
<link rel="stylesheet" href="https://fonts.googleapis.com/css2?family=Arimo:wght@400;700&display=swap">
<style>
:root{
  --red:#c00000;
  --red-dark:#8e0000;
  --top-red:#b30000;
  --ink:#222;
  --gray-text:#666;
  --light:#f6f6f6;
  --line:#c9c9c9;
  --foot-dark:#333;
  --white:#fff;
  --net-1:#0e76a8;
  --net-2:#2ca7e0;
  --net-3:#3b5998;
  --net-4:#f0a030;
}
*{margin:0;padding:0;box-sizing:border-box}
html,body{width:1200px;height:2378px;overflow:hidden;background:var(--white)}
body{position:relative;font-family:"Arimo",Arial,sans-serif;color:var(--ink)}
h1,h2,h3{font-weight:400}
.abs{position:absolute}
.topbar{left:0;top:0;width:1200px;height:27px;background:var(--top-red);color:var(--white);font-size:12.5px;text-align:right;padding:6px 46px 0 0;letter-spacing:.3px}
.topbar span{margin:0 7px}
.header{left:0;top:27px;width:1200px;height:181px;background:var(--light)}
.brand{left:58px;top:78px;display:flex;align-items:center;gap:12px}
.brand-dot{width:26px;height:26px;border-radius:50%;background:var(--red)}
.brand-name{font-size:46px;font-weight:700;color:var(--red);letter-spacing:1px}
.search{left:840px;top:63px;width:171px;height:32px;border:1px solid #ccc;background:var(--white);font-size:13px;color:#999;padding:8px 0 0 12px}
.search svg{position:absolute;right:8px;top:7px}
.social{display:flex;gap:6px}
.social i{display:flex;align-items:center;justify-content:center;width:26px;height:26px;border-radius:50%}
.social i::after{content:"";width:8px;height:8px;border-radius:50%;background:rgba(255,255,255,.9)}
.social i:nth-child(1){background:var(--net-1)}
.social i:nth-child(2){background:var(--net-2)}
.social i:nth-child(3){background:var(--net-3)}
.social i:nth-child(4){background:var(--net-4)}
.nav{left:0;top:125px;width:1200px;font-size:15px;color:#444;letter-spacing:.4px}
.nav span{position:absolute;white-space:nowrap}
.nav-active{left:304px;top:201px;width:164px;height:7px;background:#9a9a9a}
.hero{left:0;top:208px;width:1200px;height:531px;
  background:
    radial-gradient(ellipse 160px 230px at 390px 230px,rgba(226,196,140,.75),transparent 70%),
    radial-gradient(ellipse 150px 220px at 200px 210px,rgba(150,110,85,.55),transparent 70%),
    radial-gradient(ellipse 260px 260px at 620px 420px,rgba(40,48,60,.55),transparent 70%),
    radial-gradient(ellipse 220px 260px at 900px 380px,rgba(60,66,76,.5),transparent 70%),
    radial-gradient(ellipse 200px 200px at 180px 470px,rgba(70,72,78,.55),transparent 70%),
    linear-gradient(100deg,#b7c3c9 0%,#d9d6cf 35%,#e4e2de 55%,#9fa4a9 80%,#c5c8cc 100%)}
.hero-bar{left:0;top:739px;width:1200px;height:9px;background:var(--red)}
.hero-title{left:520px;top:336px;width:631px;height:62px;background:rgba(20,20,20,.8);color:var(--white);font-size:54px;font-weight:700;letter-spacing:3px;padding:4px 0 0 16px;line-height:56px}
.hero-sub{left:520px;top:404px;width:613px;height:46px;background:rgba(20,20,20,.75);color:var(--white);font-size:34px;letter-spacing:2.5px;padding:5px 0 0 16px;line-height:38px}
.btn{background:var(--red);color:var(--white);font-weight:700;display:flex;align-items:center;justify-content:center;gap:6px;letter-spacing:.5px}
.hero-btn{left:523px;top:464px;width:228px;height:56px;font-size:22px;font-weight:400;letter-spacing:1.5px}
.slide-arrow{top:415px;width:44px;height:113px;background:#555;display:flex;align-items:center;justify-content:center}
.crumb{left:55px;top:776px;font-size:12px;color:#555}
.sec-title{font-size:27px;color:var(--red);letter-spacing:1.8px}
.rule{height:1px;background:var(--line)}
.lead{left:59px;top:1124px;width:522px;font-size:14.5px;font-weight:700;color:#555;line-height:23px;text-align:justify;hyphens:auto}
.body-txt{left:59px;top:1238px;width:522px;font-size:14px;color:var(--gray-text);line-height:23px;text-align:justify;letter-spacing:.3px;hyphens:auto}
.small-btn{height:32px;font-size:12.5px}
.video{left:615px;top:873px;width:533px;height:325px;
  background:
    radial-gradient(ellipse 60px 140px at 60px 140px,rgba(245,240,230,.9),transparent 70%),
    radial-gradient(ellipse 300px 120px at 330px 260px,rgba(60,44,30,.7),transparent 75%),
    radial-gradient(ellipse 200px 60px at 300px 130px,rgba(150,140,120,.6),transparent 70%),
    linear-gradient(180deg,#f2efe8 0%,#d7cdb7 35%,#a48d6a 65%,#5e4a34 100%)}
.video-ctrl{left:615px;top:1168px;width:533px;height:30px;background:#1b1b1b}
.thumb{top:1219px;width:170px;height:119px}
.thumb-cap{top:1348px;font-size:12.5px;color:var(--red)}
.pager{top:1379px;width:25px;height:25px;background:#9a9a9a;display:flex;align-items:center;justify-content:center}
.band{left:0;top:1452px;width:1200px;height:648px;
  background:
    radial-gradient(ellipse 300px 200px at 150px 560px,rgba(160,160,160,.35),transparent 70%),
    radial-gradient(ellipse 360px 220px at 1000px 180px,rgba(170,170,170,.35),transparent 70%),
    linear-gradient(180deg,#dedede,#ebebeb 60%,#dcdcdc)}
.card-bar{top:1534px;width:249px;height:7px;background:var(--red)}
.card-img{top:1541px;width:249px;height:168px}
.card-title{font-size:21px;color:var(--red);letter-spacing:1px;line-height:22px;width:249px}
.card-txt{font-size:13px;color:#333;line-height:21px;width:249px;text-align:justify;letter-spacing:.2px;hyphens:auto}
.card-txt p+p{margin-top:21px}
.footer{left:0;top:2100px;width:1200px;height:236px;background:var(--red-dark);color:var(--white)}
.ql-title{left:52px;top:2120px;font-size:27px;letter-spacing:1.8px;color:var(--white)}
.ql-rule{left:52px;top:2159px;width:1096px;height:1px;background:rgba(255,255,255,.35)}
.ql-col{top:2180px;color:var(--white)}
.ql-col h3{font-size:15.5px;font-weight:700;letter-spacing:.8px;margin-bottom:13px;white-space:nowrap}
.ql-col li{list-style:none;font-size:12.5px;font-weight:700;line-height:26px;letter-spacing:.5px}
.ql-col li::before{content:"";display:inline-block;width:6px;height:6px;border-radius:50%;background:var(--white);margin-right:6px;vertical-align:middle}
.foot-social i{background:var(--white)!important;width:24px;height:24px}
.foot-social i::after{background:var(--red-dark)}
.bottombar{left:0;top:2336px;width:1200px;height:42px;background:var(--foot-dark);color:#ddd;font-size:13px;letter-spacing:.4px}
</style>
</head>
<body>

<div class="abs topbar"><span>Repertoire du personnel</span>|<span>Blogue</span>|<span>Solle de presse</span>|<span>Nous joindre</span>|<span>Francois</span></div>

<header class="abs header"></header>
<div class="abs brand"><i class="brand-dot"></i><span class="brand-name">KRVT</span></div>
<div class="abs search">Search
  <svg width="18" height="18" viewBox="0 0 18 18"><circle cx="7" cy="7" r="5" fill="none" stroke="#c00000" stroke-width="2.5"/><line x1="11" y1="11" x2="16" y2="16" stroke="#c00000" stroke-width="3"/></svg>
</div>
<div class="abs social" style="left:1025px;top:66px"><i></i><i></i><i></i><i></i></div>
<nav class="abs nav">
  <span style="left:308px">A propos de l'KRVT</span>
  <span style="left:494px">Programmes et Formations</span>
  <span style="left:736px">Etudians</span>
  <span style="left:833px">Nouvelles et Evenements</span>
  <span style="left:1061px">Enterprises</span>
</nav>
<div class="abs nav-active"></div>

<section class="abs hero" role="img" aria-label="Photo of smiling business students seated in a row"></section>
<div class="abs hero-bar"></div>
<div class="abs hero-title">LOREM IPSUM TEXT</div>
<div class="abs hero-sub">DUMMY SENTENCE GOES HERE</div>
<div class="abs btn hero-btn">READ MORE <svg width="22" height="12" viewBox="0 0 22 12"><path d="M0 4h14V0l8 6-8 6V8H0z" fill="#fff"/></svg></div>
<div class="abs slide-arrow" style="left:0"><svg width="16" height="26"><path d="M14 1 2 13l12 12z" fill="#fff"/></svg></div>
<div class="abs slide-arrow" style="left:1156px"><svg width="16" height="26"><path d="M2 1l12 12L2 25z" fill="#fff"/></svg></div>

<div class="abs crumb">Accueil &nbsp;&gt;&nbsp; Programmes et Formation</div>

<h1 class="abs sec-title" style="left:50px;top:813px">PROGRAMMES ET FORMATION</h1>
<div class="abs rule" style="left:48px;top:850px;width:532px"></div>
<div class="abs rule" style="left:609px;top:850px;width:542px"></div>

<div class="abs" style="left:57px;top:880px;width:526px;height:225px;background:
  radial-gradient(ellipse 60px 120px at 470px 90px,rgba(40,40,40,.7),transparent 70%),
  radial-gradient(ellipse 260px 70px at 220px 180px,rgba(40,34,30,.75),transparent 75%),
  radial-gradient(ellipse 300px 60px at 260px 110px,rgba(110,90,80,.6),transparent 75%),
  linear-gradient(180deg,#b07a4a 0%,#8c5f3a 35%,#5a4534 70%,#3a3029 100%)" role="img" aria-label="Photo of a lecturer presenting to a seated audience"></div>
<p class="abs lead">Lorem ipsum dolor sit amet, consectetur adipiscing elit. Pellentesque bibendum, lectus sit amet porta sagittis, orci eros vehicula justo, ac mollis metus felis eget dui. Nullam convallis magna dolor, non rhoncus leo faucibus vitae.</p>
<p class="abs body-txt">Donec pretium lorem quis odio euismod aliquet. Integer nec orci odio. In ullamcorper, ipsum at cursus luctus, velit tellus elementum ipsum, et feugiat dolor felis id massa. Donec dapibus rutrum elementum. Vivamus non ultricies tortor. Mauris eleifend nisl id risus lobortis bibendum. In ac egestas nibh, ut viverra magna.</p>
<div class="abs btn small-btn" style="left:59px;top:1368px;width:133px">READ MORE <svg width="14" height="8" viewBox="0 0 22 12"><path d="M0 4h14V0l8 6-8 6V8H0z" fill="#fff"/></svg></div>

<div class="abs video" role="img" aria-label="Video frame of a lecture hall with students"></div>
<svg class="abs" style="left:850px;top:1000px" width="64" height="44"><rect width="64" height="44" rx="8" fill="#1b1b1b" opacity=".85"/><path d="M26 12l14 10-14 10z" fill="#fff"/></svg>
<div class="abs video-ctrl"></div>
<div class="abs" style="left:615px;top:1168px;width:533px;height:4px;background:#555"></div>
<div class="abs" style="left:615px;top:1168px;width:40px;height:4px;background:var(--red)"></div>
<svg class="abs" style="left:630px;top:1176px" width="14" height="14"><path d="M2 1l11 6-11 6z" fill="#ccc"/></svg>
<div class="abs" style="left:690px;top:1177px;font-size:11px;color:#ccc">0:15 / 0:39</div>
<svg class="abs" style="left:1060px;top:1177px" width="80" height="14"><rect x="0" y="3" width="10" height="8" fill="#bbb"/><circle cx="26" cy="7" r="4" fill="#bbb"/><rect x="40" y="3" width="12" height="8" fill="none" stroke="#bbb" stroke-width="1.5"/><path d="M64 2h4M64 2v4M78 2h-4M78 2v4M64 12h4M64 12v-4M78 12h-4M78 12v-4" stroke="#bbb" stroke-width="1.5"/></svg>

<div class="abs thumb" style="left:615px;background:
  radial-gradient(ellipse 50px 50px at 40px 70px,rgba(30,30,35,.75),transparent 70%),
  radial-gradient(ellipse 60px 50px at 120px 75px,rgba(40,40,48,.7),transparent 70%),
  linear-gradient(180deg,#fafafa,#e6e6e6)" role="img" aria-label="Photo of business people standing in a group"></div>
<div class="abs thumb" style="left:797px;background:
  radial-gradient(ellipse 100px 30px at 95px 85px,rgba(70,55,40,.65),transparent 75%),
  linear-gradient(180deg,#f3eee2 0%,#d9cba9 45%,#9a8260 100%)" role="img" aria-label="Photo of a classroom lecture"></div>
<div class="abs thumb" style="left:978px;background:
  radial-gradient(ellipse 40px 60px at 55px 75px,rgba(235,235,235,.9),transparent 70%),
  linear-gradient(90deg,#cfc6bb 0%,#a0664a 50%,#6e2f1a 100%)" role="img" aria-label="Photo of a student in a library"></div>
<div class="abs thumb-cap" style="left:615px">Lorem Ipsum Title</div>
<div class="abs thumb-cap" style="left:797px">Lorem Ipsum Title</div>
<div class="abs thumb-cap" style="left:978px">Lorem Ipsum Title</div>
<div class="abs pager" style="left:1094px"><svg width="8" height="12"><path d="M7 1 1 6l6 5" fill="none" stroke="#fff" stroke-width="2"/></svg></div>
<div class="abs pager" style="left:1121px;background:#7a7a7a"><svg width="8" height="12"><path d="M1 1l6 5-6 5" fill="none" stroke="#fff" stroke-width="2"/></svg></div>

<section class="abs band" role="img" aria-label="Faded background photo of a classroom"></section>
<h2 class="abs sec-title" style="left:53px;top:1481px">PROGRAMMES OFFERTS</h2>
<div class="abs rule" style="left:52px;top:1517px;width:1099px;background:#bbb"></div>

<div class="abs card-bar" style="left:52px"></div>
<div class="abs card-img" style="left:52px;background:
  radial-gradient(ellipse 70px 110px at 135px 140px,rgba(205,195,175,.95),transparent 70%),
  radial-gradient(ellipse 35px 40px at 135px 55px,rgba(70,45,30,.8),transparent 70%),
  linear-gradient(180deg,#f8f8f8,#e4e0d8)" role="img" aria-label="Photo of a smiling businessman"></div>
<h3 class="abs card-title" style="left:53px;top:1720px">Executive MBA</h3>
<div class="abs card-txt" style="left:53px;top:1751px"><p>Lorem ipsum dolor sit amet, consectetur adipiscing elit. Pellentesque bibendum, lectus sit amet porta sagittis.</p><p>Lorci eros vehicula justo, ac mollis metus felis eget dui. Nullam convallis magna dolor, non rhoncus leo faucibus vitae.</p></div>
<div class="abs btn small-btn" style="left:50px;top:1954px;width:133px">READ MORE <svg width="14" height="8" viewBox="0 0 22 12"><path d="M0 4h14V0l8 6-8 6V8H0z" fill="#fff"/></svg></div>

<div class="abs card-bar" style="left:333px"></div>
<div class="abs card-img" style="left:333px;background:
  radial-gradient(ellipse 40px 120px at 70px 110px,rgba(120,170,220,.55),transparent 70%),
  radial-gradient(ellipse 50px 130px at 200px 100px,rgba(140,180,220,.5),transparent 70%),
  radial-gradient(ellipse 140px 30px at 125px 160px,rgba(230,190,110,.45),transparent 75%),
  linear-gradient(180deg,#3a6fb0,#162238)" role="img" aria-label="Photo of a city skyline of towers"></div>
<h3 class="abs card-title" style="left:333px;top:1720px">Masters of International Business</h3>
<div class="abs card-txt" style="left:333px;top:1773px"><p>Lorem ipsum dolor sit amet, consectetur adipiscing elit. Pellentesque bibendum.</p><p>Lorci eros vehicula justo, ac mollis metus felis eget dui. Nullam convallis magna dolor, non rhoncus leo faucibus vitae.</p></div>
<div class="abs btn small-btn" style="left:330px;top:1954px;width:133px">READ MORE <svg width="14" height="8" viewBox="0 0 22 12"><path d="M0 4h14V0l8 6-8 6V8H0z" fill="#fff"/></svg></div>

<div class="abs card-bar" style="left:615px"></div>
<div class="abs card-img" style="left:615px;background:
  radial-gradient(ellipse 22px 60px at 122px 120px,rgba(15,20,40,.9),transparent 70%),
  radial-gradient(ellipse 120px 60px at 180px 60px,rgba(140,190,245,.55),transparent 70%),
  linear-gradient(180deg,#3b7bd6,#123a85)" role="img" aria-label="Photo of a man facing a wall of financial charts"></div>
<h3 class="abs card-title" style="left:615px;top:1720px">Master of Finance</h3>
<div class="abs card-txt" style="left:615px;top:1751px"><p>Lorem ipsum dolor sit amet, consectetur adipiscing elit. Pellentesque bibendum, lectus sit amet porta sagittis.</p><p>Nullam convallis magna dolor, non rhoncus leo faucibus vitae.</p></div>
<div class="abs btn small-btn" style="left:612px;top:1954px;width:133px">READ MORE <svg width="14" height="8" viewBox="0 0 22 12"><path d="M0 4h14V0l8 6-8 6V8H0z" fill="#fff"/></svg></div>

<div class="abs card-bar" style="left:897px"></div>
<div class="abs card-img" style="left:897px;background:
  radial-gradient(ellipse 70px 70px at 70px 110px,rgba(40,44,55,.75),transparent 70%),
  radial-gradient(ellipse 80px 70px at 190px 100px,rgba(35,40,52,.75),transparent 70%),
  linear-gradient(180deg,#fbfbfb,#c9ced6)" role="img" aria-label="Photo of business people shaking hands"></div>
<h3 class="abs card-title" style="left:897px;top:1720px">Master of Social Entrepreneurship</h3>
<div class="abs card-txt" style="left:897px;top:1773px"><p>Lorem Pellentesque bibendum, lectus sit amet porta sagittis metus felis eget dui.</p><p>Lorci eros vehicula justo, ac mollis metus felis eget dui. Nullam convallis magna dolor, non rhoncus leo faucibus vitae.</p></div>
<div class="abs btn small-btn" style="left:894px;top:1954px;width:133px">READ MORE <svg width="14" height="8" viewBox="0 0 22 12"><path d="M0 4h14V0l8 6-8 6V8H0z" fill="#fff"/></svg></div>

<footer class="abs footer"></footer>
<h2 class="abs ql-title">QUICKLINKS</h2>
<div class="abs ql-rule"></div>
<div class="abs ql-col" style="left:94px"><h3>A propos de l'KRVT</h3><ul><li>Sublink 1</li><li>Sublink 2</li><li>Sublink 3</li><li>Sublink 4</li></ul></div>
<div class="abs ql-col" style="left:279px"><h3>Programmes et Formations</h3><ul><li>Sublink 1</li><li>Sublink 2</li><li>Sublink 3</li><li>Sublink 4</li></ul></div>
<div class="abs ql-col" style="left:534px"><h3>Etudians</h3><ul><li>Sublink 1</li><li>Sublink 2</li><li>Sublink 3</li><li>Sublink 4</li></ul></div>
<div class="abs ql-col" style="left:662px"><h3>Nouvelles et Evenements</h3><ul><li>Sublink 1</li><li>Sublink 2</li><li>Sublink 3</li><li>Sublink 4</li></ul></div>
<div class="abs ql-col" style="left:930px"><h3>Enterprises</h3><ul><li>Sublink 1</li><li>Sublink 2</li><li>Sublink 3</li></ul></div>
<div class="abs social foot-social" style="left:930px;top:2295px"><i></i><i></i><i></i><i></i></div>

<div class="abs bottombar">
  <span class="abs" style="left:79px;top:13px">Sitemap &nbsp; / &nbsp; FAQ &nbsp; / &nbsp; Privacy Policy</span>
  <span class="abs" style="left:982px;top:13px">Copyright © 2014 KRVT</span>
</div>

</body>
</html>
```